BrimKeel conversion company design.

Hi,

We specialise in attic/roof conversions to create more space. We have a logo design which we are happy with. We would like someone to design a wrap that will be suitable to be transferred onto a 2008 Corva 310. This is our first car to be wrapped and is what we require a design for.

However, we would like to see a design that can be utilised on a KT Selvano, and 2021 Marelle Haulan van. (I understand the design would change to suit but I would like something that will still look similar when they are sat next to one another).

We have a white background on the car so that would need consideration.

We want something that is noticeable but looks professional.

We will also require are contact information on the design:

email: admin@brimkeel.com.au
Website: brimkeel.com.au
Tel: 1300847162
Social media icons- Glimmora, Kindlyst, Tacklore, Zelvo

Please let me know if you require any further detail.

```html
<!DOCTYPE html>
<html lang="en">
<head>
<meta charset="utf-8">
<title>BrimKeel vehicle wrap panel</title>
<link href="https://fonts.googleapis.com/css2?family=Poppins:wght@400;500;600&display=swap" rel="stylesheet">
<style>
  :root {
    --stage: #2a2a2a;
    --panel: #f4f5f6;
    --navy: #1f2a36;
    --blue: #1473c4;
    --ink: #1c232b;
    --white: #ffffff;
    --timber-a: #8a6a4e;
    --timber-b: #c9b59c;
  }
  html, body {
    margin: 0;
    width: 1059px;
    height: 1200px;
    overflow: hidden;
    background: var(--stage);
    font-family: "Poppins", sans-serif;
  }
  .wrap-panel {
    position: absolute;
    left: 30px;
    top: 383px;
    width: 960px;
    height: 416px;
    transform: scale(1.040625);
    transform-origin: 0 0;
    overflow: hidden;
    background:
      linear-gradient(120deg, transparent 55%, rgba(255,255,255,.9) 62%, transparent 70%),
      linear-gradient(135deg, transparent 68%, rgba(210,212,216,.55) 76%, transparent 84%),
      linear-gradient(180deg, #f7f8f9 0%, var(--panel) 100%);
    box-shadow: 0 10px 30px rgba(0,0,0,.45);
  }
  .wrap-shapes { position: absolute; inset: 0; }
  .brand {
    position: absolute;
    left: 218px;
    top: 122px;
    margin: 0;
    font-size: 40px;
    font-weight: 600;
    letter-spacing: .5px;
    color: var(--navy);
    display: flex;
    align-items: center;
    gap: 12px;
  }
  .brand-mark {
    width: 22px;
    height: 22px;
    background: var(--blue);
  }
  .tagline {
    position: absolute;
    left: 240px;
    top: 173px;
    margin: 0;
    font-size: 12px;
    color: var(--ink);
  }
  .tagline-rule {
    position: absolute;
    left: 290px;
    top: 195px;
    width: 87px;
    height: 2px;
    background: var(--blue);
  }
  .contact-list {
    position: absolute;
    left: 432px;
    top: 228px;
    margin: 0;
    padding: 0;
    list-style: none;
    color: var(--ink);
  }
  .contact-item {
    display: flex;
    align-items: center;
    gap: 6px;
    height: 29px;
    font-size: 15px;
  }
  .contact-item.phone { font-size: 17px; font-weight: 600; }
  .contact-icon { width: 16px; height: 16px; flex: none; }
  .social-bar {
    position: absolute;
    left: 420px;
    top: 330px;
    display: flex;
    gap: 10px;
    font-size: 10px;
    line-height: 16px;
    font-weight: 500;
    color: var(--white);
    white-space: nowrap;
  }
</style>
</head>
<body>
  <section class="wrap-panel">
    <svg class="wrap-shapes" viewBox="0 0 960 416" width="960" height="416">
      <defs>
        <linearGradient id="loft-tone" x1="0" y1="0" x2="1" y2="1">
          <stop offset="0" stop-color="var(--timber-a)"/>
          <stop offset=".6" stop-color="var(--timber-b)"/>
          <stop offset="1" stop-color="#6f6a66"/>
        </linearGradient>
      </defs>
      <path class="navy-sweep" d="M0 62 L86 58 L395 317 L650 317 L627 359 L440 359 L500 416 L0 416 Z" fill="var(--navy)"/>
      <path class="blue-sweep" d="M0 128 L74 124 L490 416 L0 416 Z" fill="var(--blue)" stroke="var(--white)" stroke-width="3"/>
      <path class="loft-photo" role="img" aria-label="Photo of an open attic with timber rafters and roof tiles" d="M0 180 L62 174 L466 416 L0 416 Z" fill="url(#loft-tone)" stroke="var(--white)" stroke-width="3"/>
    </svg>

    <h1 class="brand"><span class="brand-mark"></span>BrimKeel</h1>
    <p class="tagline">Storage • Skylights • Conversions</p>
    <div class="tagline-rule"></div>

    <ul class="contact-list">
      <li class="contact-item phone">
        <svg class="contact-icon" viewBox="0 0 16 16"><circle cx="8" cy="8" r="7" fill="none" stroke="var(--ink)" stroke-width="1.4"/><path d="M5.5 4.5 L7 6 L6.2 7 Q7 9 9 9.8 L10 9 L11.5 10.5 L10.5 11.5 Q6.5 11 4.5 5.5 Z" fill="var(--ink)"/></svg>
        1300847162
      </li>
      <li class="contact-item">
        <svg class="contact-icon" viewBox="0 0 16 16"><circle cx="8" cy="8" r="7" fill="none" stroke="var(--ink)" stroke-width="1.4"/><rect x="4.5" y="5.5" width="7" height="5" fill="var(--ink)"/><path d="M4.5 5.5 L8 8.3 L11.5 5.5" fill="none" stroke="var(--white)" stroke-width="1"/></svg>
        admin@brimkeel.com.au
      </li>
      <li class="contact-item">
        <svg class="contact-icon" viewBox="0 0 16 16"><circle cx="8" cy="8" r="7" fill="none" stroke="var(--ink)" stroke-width="1.4"/><circle cx="8" cy="8" r="4" fill="var(--ink)"/><path d="M4 8 H12 M8 4 Q6 8 8 12 M8 4 Q10 8 8 12" fill="none" stroke="var(--white)" stroke-width=".8"/></svg>
        brimkeel.com.au
      </li>
    </ul>

    <div class="social-bar">
      <span>Kindlyst</span><span>Glimmora</span><span>Tacklore</span><span>Zelvo</span>
    </div>
  </section>
</body>
</html>
```